Need a label for food product looking original design

We need two labels designed ( Front and Back ) for our new product Freeze Dried Strawberry Pieces On the front should also be our company name Velmaro . A pack will weigh 50 grams there should also be an image included of these strawbberies please find an attached file. Also it's suitable for vegans and vegetarians On the back there should be some information included what the product is used for and nutritional facts, also an e-mail for questions or product quality to be sent to sales@velmaro.co.uk Both labels should be 16cm long and 11cm wide we'll be using stand up pouches.

Target Market(s)

Bakery, snacks.

Font styles to use
Decorative
Script

Requirements
Must have
• Company name, image of the product.Label color to blend in pouch color.
Nice to have
• Suitable for vegans and vegetarians logos.
Should not have
• Custom printed pouches are not available.

```html
<!DOCTYPE html>
<html lang="en">
<head>
<meta charset="utf-8">
<title>Velmaro Freeze Dried Strawberry Pieces – Label</title>
<link rel="stylesheet" href="https://fonts.googleapis.com/css2?family=Kaushan+Script&family=Dancing+Script:wght@400;500;600&family=Cormorant+Garamond:wght@400;500&family=Open+Sans:wght@700&display=swap">
<style>
  :root {
    --bg: #e4e3e4;
    --paper: #ffffff;
    --berry: #e6244b;
    --berry-soft: #e8637b;
    --band: #ef4560;
    --ink: #1d1d1d;
    --badge: #1f6b2f;
  }
  * { margin: 0; padding: 0; box-sizing: border-box; }
  html, body { width: 1200px; height: 963px; overflow: hidden; background: var(--bg); }
  .canvas { position: relative; width: 1200px; height: 963px; }
  .label { position: absolute; top: 67px; background: var(--paper); overflow: hidden; }
  .label--front { left: 28px; width: 559px; height: 829px; }
  .label--back { left: 610px; width: 561px; height: 830px; }

  /* front */
  .front-wave { position: absolute; left: 0; top: 0; width: 559px; height: 360px; }
  .title { position: absolute; color: #fff; font-family: "Kaushan Script", cursive; font-weight: 400; white-space: nowrap; line-height: 1; }
  .title--freeze { left: 53px; top: 36px; font-size: 90px; letter-spacing: -1px; }
  .title--strawberry { left: 94px; top: 140px; font-size: 76px; }
  .title--pieces { left: 314px; top: 232px; font-size: 76px; }

  .claims { position: absolute; left: 0; top: 0; font-family: "Dancing Script", cursive; font-weight: 500; color: var(--berry); font-size: 31px; line-height: 1; }
  .claim { position: absolute; white-space: nowrap; }
  .claim--1 { left: 63px; top: 347px; }
  .claim--2 { left: 85px; top: 388px; }
  .claim--3 { left: 110px; top: 429px; }

  .vegan-badge { position: absolute; left: 377px; top: 416px; width: 78px; height: 78px; border-radius: 50%; background: var(--badge); }

  .product-photo { position: absolute; left: 0; top: 487px; width: 424px; height: 273px; background: radial-gradient(ellipse at 45% 50%, #d93a55 0%, #e0566f 55%, #f3c3cc 100%); }

  .net-weight { position: absolute; left: 57px; top: 773px; font-family: "Cormorant Garamond", serif; font-size: 24px; color: var(--berry); letter-spacing: 2px; }
  .brand-name { position: absolute; left: 362px; top: 754px; font-family: "Cormorant Garamond", serif; font-weight: 500; font-size: 43px; color: var(--berry); }

  /* back */
  .headline-arc { position: absolute; left: 0; top: 40px; width: 561px; height: 120px; overflow: visible; }
  .headline-arc text { font-family: "Dancing Script", cursive; font-size: 46px; font-weight: 500; fill: var(--berry); }
  .fruit-photo { position: absolute; left: 238px; top: 112px; width: 106px; height: 188px; background: linear-gradient(180deg, #e6515a 0%, #d8262c 55%, #c01f24 100%); }
  .side-note { position: absolute; top: 160px; font-family: "Dancing Script", cursive; font-size: 21px; line-height: 26.5px; color: var(--ink); }
  .side-note--left { left: 44px; width: 176px; text-align: center; }
  .side-note--right { right: 48px; width: 160px; text-align: right; }

  .usage-band { position: absolute; left: 0; top: 347px; width: 561px; height: 330px; background: var(--band); }
  .usage-text { position: absolute; left: 66px; top: 28px; width: 431px; font-family: "Dancing Script", cursive; font-weight: 600; font-size: 31px; line-height: 39.5px; color: #fff; }
  .usage-line { display: block; white-space: nowrap; }
  .usage-line--full { text-align: justify; text-align-last: justify; }

  .contact-label { position: absolute; left: 52px; top: 727px; font-family: "Dancing Script", cursive; font-size: 22px; color: var(--berry); }
  .contact-email { position: absolute; left: 52px; top: 770px; font-family: "Open Sans", sans-serif; font-weight: 700; font-size: 22px; color: var(--berry); }
  .origin { position: absolute; right: 50px; top: 765px; font-family: "Dancing Script", cursive; font-size: 26px; color: var(--berry); }
</style>
</head>
<body>
<div class="canvas">

  <section class="label label--front">
    <svg class="front-wave" viewBox="0 0 559 360" preserveAspectRatio="none" aria-hidden="true">
      <defs>
        <linearGradient id="frontBand" x1="0" y1="0" x2="1" y2="0">
          <stop offset="0" stop-color="#e6244b"/>
          <stop offset="1" stop-color="#e9637c"/>
        </linearGradient>
      </defs>
      <path d="M0 0 H559 V355 C470 350 380 345 300 320 C230 300 170 292 120 302 C70 312 30 328 0 340 Z" fill="url(#frontBand)"/>
    </svg>
    <h1>
      <span class="title title--freeze">Freeze Dried</span>
      <span class="title title--strawberry">strawberry</span>
      <span class="title title--pieces">pieces</span>
    </h1>
    <div class="claims">
      <span class="claim claim--1">100% strawberry</span>
      <span class="claim claim--2">no suggar added</span>
      <span class="claim claim--3">no preservatives</span>
    </div>
    <div class="vegan-badge" role="img" aria-label="Suitable for vegans and vegetarians badge"></div>
    <div class="product-photo" role="img" aria-label="Photo of a pile of freeze dried strawberry pieces"></div>
    <p class="net-weight">Net 50g</p>
    <p class="brand-name">Velmaro</p>
  </section>

  <section class="label label--back">
    <svg class="headline-arc" viewBox="0 0 561 120" aria-label="Tastes like the original fruit">
      <path id="arcPath" d="M50 94 Q270 0 520 84" fill="none"/>
      <text><textPath href="#arcPath" startOffset="0">Tastes like the original fruit</textPath></text>
    </svg>
    <p class="side-note side-note--left">50g of freeze-dried<br>strawberries is the<br>equivalent of 500gr<br>of strawberries.<br>Just the water is<br>taken away.</p>
    <div class="fruit-photo" role="img" aria-label="Photo of a whole fresh strawberry"></div>
    <p class="side-note side-note--right">You can eat as-is,<br>or rehydrate if<br>you wish.<br>Eat as a snack, or<br>add to muesli.</p>

    <div class="usage-band">
      <p class="usage-text">
        <span class="usage-line usage-line--full">Freeze-dried strawberries are a</span>
        <span class="usage-line">delicious natural fruit snack,</span>
        <span class="usage-line usage-line--full">but they are also an ideal way for</span>
        <span class="usage-line">manufacturers to add the natural</span>
        <span class="usage-line usage-line--full">fresh appeal of fruit to food</span>
        <span class="usage-line">products such as breakfast cereals,</span>
        <span class="usage-line">cereal bars, chocolate and fruit teas</span>
      </p>
    </div>

    <p class="contact-label">Questions or product quality</p>
    <p class="contact-email">sales@velmaro.co.uk</p>
    <p class="origin">Packed in the UK.</p>
  </section>

</div>
</body>
</html>
```